Business Card Design

After a corporate career in the finance sector I am now operating on my own as a consultant. I require a simple design, and want a strong card which is targeted at a conservative audience.

Target Market(s)

highly educated senior management, directors of companies, finance sector

Industry/Entity Type

Conservative

Contact Information for Business Card

Rosa Tindell
Consultant
Mobile: 0417 862 254
Email: rosa.tind@mailvora.com

Requirements
Should not have
• I don't want the colours green/yellow/brown

```html
<!DOCTYPE html>
<html lang="en">
<head>
<meta charset="utf-8">
<title>Rosa Tindell — Business Card</title>
<link rel="stylesheet" href="https://fonts.googleapis.com/css2?family=Open+Sans:wght@400;500&display=swap">
<style>
  :root {
    --backdrop: #4a3a34;
    --card-paper: #dcd8d0;
    --card-paper-light: #e3dfd8;
    --ink-dark: #161616;
    --ink-muted: #6e6b66;
  }
  html, body {
    margin: 0;
    padding: 0;
    width: 1200px;
    height: 900px;
    overflow: hidden;
    background: var(--backdrop);
  }
  .stage {
    width: 1200px;
    height: 900px;
    display: flex;
    align-items: center;
    justify-content: center;
  }
  .business-card {
    position: relative;
    width: 840px;
    height: 480px;
    background: linear-gradient(160deg, var(--card-paper-light) 0%, var(--card-paper) 100%);
    box-shadow: 0 6px 18px rgba(0, 0, 0, 0.35);
    font-family: "Open Sans", Arial, sans-serif;
  }
  .contact-block {
    position: absolute;
    right: 46px;
    top: 168px;
    text-align: right;
    line-height: 1.25;
  }
  .holder-name {
    margin: 0;
    font-size: 23px;
    font-weight: 500;
    color: var(--ink-dark);
  }
  .holder-role {
    margin: 0 0 18px;
    font-size: 17px;
    font-weight: 400;
    color: var(--ink-dark);
  }
  .contact-line {
    margin: 0;
    font-size: 18px;
    font-weight: 400;
    color: var(--ink-muted);
  }
</style>
</head>
<body>
  <main class="stage">
    <section class="business-card">
      <div class="contact-block">
        <h1 class="holder-name">Rosa Tindell</h1>
        <p class="holder-role">Consultant</p>
        <p class="contact-line contact-phone">0417 862 254</p>
        <p class="contact-line contact-email">rosa.tind@mailvora.com</p>
      </div>
    </section>
  </main>
</body>
</html>
```